A new presentation to our clients

we are a Real Estate agency, our website is www.dorelumia.com and it’s time to have a new, fashion and remarcable Business Card. we want to differentiate ourselves from other companies so we want a business card that differentiates us. we want the business card to impact our customers. in the competitive market that we have today, we have to be different and it is this difference that we seek

Target Market(s)

Real Estate Clients

Contact Information for Business Card

We search a totaly diferent card from the usual

Font styles to use
Sans Serif

Colors
e34197

Requirements
Must have
• Logo, adress, phone contact, e-mail, photo, and our website
Nice to have
• We would like to see a modern business card
Should not have
• Houses or building draws

```html
<!DOCTYPE html>
<html lang="pt">
<head>
<meta charset="utf-8">
<title>Dore Lumia – Cartão de Visita</title>
<link href="https://fonts.googleapis.com/css2?family=Roboto:wght@400;500;700&display=swap" rel="stylesheet">
<style>
  :root {
    --brand-pink: #d81b6f;
    --card-white: #f1f1f2;
    --card-grey: #e3e3e5;
    --ink-dark: #3a3a3c;
    --text-light: #ffffff;
    --backdrop: #2b2b2d;
  }
  * { box-sizing: border-box; margin: 0; padding: 0; }
  html, body { width: 1200px; height: 800px; overflow: hidden; }
  body {
    background: var(--backdrop);
    font-family: "Roboto", Arial, sans-serif;
    position: relative;
  }
  .card {
    position: absolute;
    width: 525px;
    height: 300px;
    background: linear-gradient(135deg, var(--card-white) 0%, var(--card-grey) 55%, var(--card-white) 100%);
    overflow: hidden;
  }
  .card-front { left: 150px; top: 60px; }
  .card-back { left: 525px; top: 440px; }

  .brand-name {
    position: absolute;
    color: var(--brand-pink);
    font-weight: 500;
    white-space: nowrap;
  }
  .card-front .brand-name {
    left: 0; right: 0; top: 100px;
    text-align: center;
    font-size: 52px;
  }
  .front-band {
    position: absolute; left: 0; right: 0;
    top: 212px; height: 34px;
    background: var(--brand-pink);
    display: flex; align-items: center; justify-content: center;
  }
  .front-band .website {
    color: var(--text-light);
    font-size: 14px;
    letter-spacing: 3px;
  }
  .front-stripe {
    position: absolute; left: 0; right: 0;
    top: 266px; height: 20px;
    background: var(--brand-pink);
  }

  .card-back .brand-name {
    left: 28px; top: 146px;
    font-size: 36px;
  }
  .contact-panel {
    position: absolute;
    left: 270px; top: 0;
    width: 195px; height: 300px;
    background: var(--brand-pink);
  }
  .panel-title {
    position: absolute; left: 300px; top: 26px;
    color: var(--text-light);
  }
  .panel-title .company { font-size: 17px; font-weight: 700; }
  .panel-title .tagline { font-size: 11px; letter-spacing: 0.5px; margin-top: 2px; }

  .contact-list {
    position: absolute; left: 258px; top: 110px;
    list-style: none;
  }
  .contact-list li {
    display: flex; align-items: center;
    height: 28px; margin-bottom: 4px;
    color: var(--text-light);
    font-size: 12px;
  }
  .contact-list .icon {
    width: 26px; height: 26px;
    background: var(--ink-dark);
    display: flex; align-items: center; justify-content: center;
    margin-right: 18px;
  }
  .contact-list li.fax-row {
    background: var(--ink-dark);
    width: 250px;
  }
  .address-bar {
    position: absolute;
    left: 0; right: 0; top: 248px; height: 30px;
    background: var(--ink-dark);
    display: flex; align-items: center;
    padding-left: 30px;
    color: var(--text-light);
    font-size: 13px;
    letter-spacing: 0.4px;
  }
  .address-bar::before {
    content: "";
    position: absolute; left: 0; top: 0;
    width: 10px; height: 30px;
    background: var(--brand-pink);
  }
  .address-bar svg { margin-right: 8px; }
</style>
</head>
<body>

<section class="card card-front" aria-label="Frente do cartão">
  <div class="brand-name">Dore Lumia</div>
  <div class="front-band"><span class="website">www.dorelumia.com</span></div>
  <div class="front-stripe"></div>
</section>

<section class="card card-back" aria-label="Verso do cartão">
  <div class="brand-name">Dore Lumia</div>
  <div class="contact-panel"></div>
  <div class="panel-title">
    <div class="company">Dore Lumia</div>
    <div class="tagline">Mediação Imobiliária</div>
  </div>
  <ul class="contact-list">
    <li>
      <span class="icon"><svg width="12" height="12" viewBox="0 0 24 24"><path fill="#fff" d="M6.6 10.8a15 15 0 0 0 6.6 6.6l2.2-2.2a1 1 0 0 1 1-.25 11.4 11.4 0 0 0 3.6.57 1 1 0 0 1 1 1V20a1 1 0 0 1-1 1A17 17 0 0 1 3 4a1 1 0 0 1 1-1h3.5a1 1 0 0 1 1 1c0 1.25.2 2.45.57 3.57a1 1 0 0 1-.25 1z"/></svg></span>
      (+351) 210 555 140
    </li>
    <li>
      <span class="icon"><svg width="13" height="10" viewBox="0 0 26 20"><rect x="1" y="1" width="24" height="18" fill="none" stroke="#fff" stroke-width="2"/><path d="M1 1l12 10 12-10" fill="none" stroke="#fff" stroke-width="2"/></svg></span>
      geral@dorelumia.com
    </li>
    <li>
      <span class="icon"><svg width="13" height="13" viewBox="0 0 24 24"><circle cx="12" cy="12" r="10" fill="none" stroke="#fff" stroke-width="2"/><path d="M2 12h20M12 2c3 3 3 17 0 20M12 2c-3 3-3 17 0 20" fill="none" stroke="#fff" stroke-width="1.6"/></svg></span>
      www.dorelumia.com
    </li>
    <li class="fax-row">
      <span class="icon"><svg width="13" height="13" viewBox="0 0 24 24"><rect x="6" y="2" width="12" height="6" fill="#fff"/><rect x="2" y="9" width="20" height="9" fill="#fff"/><rect x="6" y="15" width="12" height="7" fill="#fff" stroke="#3a3a3c" stroke-width="1.5"/></svg></span>
      (+351) 210 555 149
    </li>
  </ul>
  <div class="address-bar">
    <svg width="11" height="15" viewBox="0 0 12 16"><path fill="#fff" d="M6 0a6 6 0 0 0-6 6c0 4.5 6 10 6 10s6-5.5 6-10a6 6 0 0 0-6-6zm0 8.5A2.5 2.5 0 1 1 6 3.5a2.5 2.5 0 0 1 0 5z"/></svg>
    Rua das Acácias, 118 4400-512, Vila Nova de Gaia
  </div>
</section>

</body>
</html>
```